Brivolt: Electrical Contractor flyer design.

We are looking for a sharp and professional flyer to promote the business's cost for specific jobs and to promote the business.
We are a small electrical business looking to break into the market.
Attached logo to be used and following content to be incorporated. Contact details will be given upon final flyer design.

Internal Power Points: $ 120
External Weather Proof Power Points: $150
T.V. Points: $120 (excludes aerial)
T.V. Mounting: $ 200 (Exclude Leads)
Aerials Starting From: $220 Incudes Mast
LED Down lights: $60 per unti
Ceiling Fans: $150 (Fan Excluded)
Oven & Range Hood Change Overs: $250
A.C. Install: $300
S/B Upgrade: From $600
Safety Switch Installation: $280
Phone Points: $120

Services Incude:

New home wiring
Shop & Office Fit Outs
Re - Wires
Extentions
Garden Lighting
Home Thearters
Home Automation
Power Points
Phone, Data
Feature Lighting
Lighting design and Installation
Ceiling Fans
A.C Installation
Oven & Range hood Installation

*All prices are gst inclusive
**Prices subject to change due to site access.

```html
<!DOCTYPE html>
<html lang="en">
<head>
<meta charset="utf-8">
<title>Brivolt – Electrical Contractor Flyer</title>
<link href="https://fonts.googleapis.com/css2?family=Mulish:wght@300;400;800&family=Ubuntu:wght@700&family=Open+Sans:wght@700&display=swap" rel="stylesheet">
<style>
  :root {
    --orange: #e8692a;
    --orange-light: #ef7f3f;
    --charcoal: #3a3a3c;
    --charcoal-light: #5a5a5c;
    --ink: #111111;
    --white: #ffffff;
    --stage: #b8b8b8;
    --logo-grey: #4a4a4c;
  }
  * { box-sizing: border-box; margin: 0; padding: 0; }
  html, body { width: 1200px; height: 758px; overflow: hidden; }
  body {
    background: var(--stage);
    font-family: "Mulish", sans-serif;
    position: relative;
  }
  .flyer {
    position: absolute;
    left: 0; top: 96px;
    width: 1200px; height: 565px;
    background: var(--white);
    overflow: hidden;
  }
  .header { position: absolute; left: 0; top: 0; width: 1200px; height: 111px; }
  .header svg { position: absolute; inset: 0; }
  .brand {
    position: absolute; left: 56px; top: 30px;
    display: flex; align-items: center; gap: 12px;
  }
  .brand-mark { width: 26px; height: 26px; background: var(--orange); }
  .brand-name {
    font-family: "Mulish", sans-serif; font-weight: 800;
    font-size: 44px; color: var(--logo-grey); letter-spacing: 1px; line-height: 1;
  }
  .tagline {
    position: absolute; right: 20px; top: 20px;
    text-align: right; color: var(--white);
    font-weight: 300; font-size: 29px; line-height: 39px; letter-spacing: 0.3px;
  }
  .photos { position: absolute; top: 111px; left: 0; width: 1200px; height: 243px; }
  .photo { position: absolute; top: 0; height: 243px; }
  .photo-house { left: 0; width: 387px; background: linear-gradient(180deg, #0e1220 0%, #1d1e26 45%, #8a6a48 70%, #3b3a2c 100%); }
  .photo-shelf { left: 387px; width: 425px; background: linear-gradient(90deg, #cfcfcf 0%, #9a9a9a 45%, #d8d8d8 100%); }
  .photo-wiring { left: 812px; width: 388px; background: linear-gradient(160deg, #2f5a94 0%, #5d86bf 40%, #a9a28a 70%, #6e7a4a 100%); }
  .info { position: absolute; top: 354px; left: 0; width: 1200px; height: 186px; }
  .info svg { position: absolute; inset: 0; }
  .section-title {
    position: absolute; font-family: "Ubuntu", sans-serif; font-weight: 700;
    font-size: 20px; letter-spacing: 0.3px;
  }
  .products-title { left: 29px; top: 12px; color: var(--white); }
  .services-title { left: 738px; top: 12px; color: var(--ink); }
  .list { position: absolute; list-style: none; font-size: 14px; line-height: 20.4px; }
  .list li { display: flex; align-items: center; gap: 5px; white-space: nowrap; }
  .products .list { color: var(--white); }
  .products .list li::before {
    content: ""; width: 9px; height: 9px; border: 2px solid var(--white);
    border-radius: 50%; flex: none;
  }
  .services .list { color: var(--white); }
  .services .list li { gap: 7px; }
  .services .list li::before {
    content: ""; width: 11px; height: 11px; background: var(--ink);
    border-radius: 50%; flex: none;
  }
  .col-a { left: 29px; top: 37px; }
  .col-b { left: 345px; top: 37px; }
  .col-c { left: 722px; top: 37px; }
  .col-d { left: 933px; top: 37px; }
  .footer {
    position: absolute; left: 0; top: 540px; width: 1200px; height: 25px;
    background: var(--white); display: flex; align-items: center;
    font-family: "Open Sans", sans-serif; font-weight: 700; font-size: 13px; color: var(--ink);
  }
  .footer span { position: absolute; }
  .footer .address { left: 58px; }
  .footer .phone { left: 547px; }
  .footer .social { left: 814px; }
</style>
</head>
<body>
  <main class="flyer">
    <header class="header">
      <svg width="1200" height="111" viewBox="0 0 1200 111" aria-hidden="true">
        <rect width="1200" height="111" fill="var(--white)"/>
        <polygon points="361,0 1200,0 1200,111 266,111" fill="var(--orange)"/>
        <polygon points="361,0 1200,0 1200,68 320,68" fill="var(--orange-light)" opacity="0.35"/>
      </svg>
      <div class="brand">
        <span class="brand-mark"></span>
        <span class="brand-name">Brivolt</span>
      </div>
      <p class="tagline">DOMESTIC AND COMMERCIAL ELECTRICAL COMPANY<br>BASED IN MELBOURNE'S SOUTH EAST</p>
    </header>

    <section class="photos">
      <div class="photo photo-house" role="img" aria-label="Photo of a modern brick house lit up at night"></div>
      <div class="photo photo-shelf" role="img" aria-label="Black and white photo of wine bottles on a shelf with LED strip lighting"></div>
      <div class="photo photo-wiring" role="img" aria-label="Close-up photo of blue wires in a switchboard terminal block"></div>
    </section>

    <section class="info">
      <svg width="1200" height="186" viewBox="0 0 1200 186" aria-hidden="true">
        <defs>
          <linearGradient id="darkFill" x1="0" y1="0" x2="0" y2="1">
            <stop offset="0" stop-color="#343436"/>
            <stop offset="1" stop-color="#5e5e60"/>
          </linearGradient>
          <linearGradient id="orangeFill" x1="0" y1="0" x2="0" y2="1">
            <stop offset="0" stop-color="#e4621f"/>
            <stop offset="1" stop-color="#ee8a4e"/>
          </linearGradient>
        </defs>
        <rect width="1200" height="186" fill="url(#darkFill)"/>
        <polygon points="699,0 1200,0 1200,186 640,186" fill="url(#orangeFill)"/>
      </svg>

      <div class="products">
        <h2 class="section-title products-title">PRODUCTS AVAILABLE</h2>
        <ul class="list col-a">
          <li>Internal Power Points: $ 120</li>
          <li>External Weather Proof Power Points: $150</li>
          <li>T.V. Points: $120 (excludes aerial)</li>
          <li>T.V. Mounting: $ 200 (Exclude Leads)</li>
          <li>Aerials Starting From: $220 Incudes Mast</li>
          <li>LED Down lights: $60 per unit</li>
        </ul>
        <ul class="list col-b">
          <li>Ceiling Fans: $150 (Fan Excluded)</li>
          <li>Oven &amp; Range Hood Change Overs: $250</li>
          <li>A.C. Install: $300</li>
          <li>S/B Upgrade: From $600</li>
          <li>Safety Switch Installation: $280</li>
          <li>Phone Points: $120</li>
        </ul>
      </div>

      <div class="services">
        <h2 class="section-title services-title">SERVICES INCUDE</h2>
        <ul class="list col-c">
          <li>New home wiring</li>
          <li>Shop &amp; Office Fit Outs</li>
          <li>Re - Wires</li>
          <li>Extentions</li>
          <li>Garden Lighting</li>
          <li>Home Thearters</li>
          <li>Home Automation</li>
        </ul>
        <ul class="list col-d">
          <li>Power Points</li>
          <li>Phone, Data</li>
          <li>Feature Lighting</li>
          <li>Lighting design and Installation</li>
          <li>Ceiling Fans</li>
          <li>A.C Installation</li>
          <li>Oven &amp; Range hood Installation</li>
        </ul>
      </div>
    </section>

    <footer class="footer">
      <span class="address">Address: Brivolt Pty Ltd, Larkfield, Victoria, Australia 3999</span>
      <span class="phone">Phone: +61 400 812 356</span>
      <span class="social">Social: https://web.circlefeed.net/Brivolt</span>
    </footer>
  </main>
</body>
</html>
```